Redesign of Engineering firm website

I want a redesign of the torvelpower.com website with the below in mind:

1- the client has a 3 main sectors: Renewable Energy, Process Automation and General Engineering.
2- Home page should show the 3 sectors
3- the other standard pages should be home, About, Clients, Projects, Training, Career, and Contact
4- The theme should be wordpress.
5- Responsive layout that works with all devices
6- One page layout is preferable for the home page.
7- it should be original and is not copied from other templates.
Updates

Reason: As requested from so many designers... the deadline is extended. Thank you

Target Market(s)

Engineers and professional

Industry/Entity Type

Solar Energy

Font styles to use
Serif
Sans Serif

Colors
3277b5
0355a3
0493ce

Requirements
Must have
• pictures that represent the three sectors

```html
<!DOCTYPE html>
<html lang="en">
<head>
<meta charset="utf-8">
<title>Torvel – Renewable Energy, Process Automation, General Engineering</title>
<link href="https://fonts.googleapis.com/css2?family=Open+Sans:wght@400;600;700&family=Roboto+Slab:wght@300;400&family=Raleway:wght@400;500&display=swap" rel="stylesheet">
<style>
:root{
  --blue:#3277b5;
  --blue-dark:#0355a3;
  --blue-light:#0493ce;
  --band:#2d80d2;
  --yellow:#f7b500;
  --green:#5fb83a;
  --ink:#222;
  --muted:#666;
  --line:#dcdcdc;
  --footer:#121212;
  --footer-deep:#070707;
}
*{margin:0;padding:0;box-sizing:border-box}
html,body{width:1200px;height:3183px;overflow:hidden}
body{position:relative;font-family:"Open Sans",Arial,sans-serif;color:var(--ink);background:#fff}

/* header */
.site-header{position:absolute;top:0;left:0;width:1200px;height:75px;z-index:5}
.site-header svg{position:absolute;top:0;left:0}
.brand{position:absolute;left:78px;top:8px;font:700 40px/1 "Open Sans",sans-serif;color:var(--blue-light);letter-spacing:1px}
.main-nav{position:absolute;top:40px;left:546px;display:flex}
.main-nav a{color:#fff;text-decoration:none;font-size:14px;margin-right:29px}
.main-nav a.active{color:var(--yellow)}
.social{position:absolute;display:flex;gap:22px}
.social span{width:14px;height:14px;border-radius:50%;background:#fff;display:block}

/* hero */
.hero{position:absolute;top:0;left:0;width:1200px;height:560px;overflow:hidden}
.hero-photo{position:absolute;inset:0;background:linear-gradient(180deg,#3e5675 0%,#6d7f95 28%,#c79b6a 42%,#2c4f7c 55%,#15325d 100%)}
.hero h1{position:absolute;left:84px;top:160px;width:700px;color:#fff;font:700 43px/52px "Open Sans",sans-serif}
.hero p{position:absolute;left:84px;top:272px;width:800px;color:#fff;font-size:15px;line-height:25px}
.btn{display:inline-block;background:var(--yellow);color:#222;font:600 13px/28px "Open Sans",sans-serif;padding:0 16px;text-decoration:none}
.hero .btn{position:absolute;left:85px;top:370px}
.dots{position:absolute;top:489px;left:577px;display:flex;gap:14px}
.dots span{width:11px;height:11px;border-radius:50%;background:#d6d6d6}
.hero-wave{position:absolute;left:0;bottom:0}

/* sectors */
.section-title{position:absolute;width:1200px;text-align:center;font:600 28px/1 "Open Sans",sans-serif;color:#111}
.section-title em{font-style:normal;color:var(--blue-light)}
.sector-card{position:absolute;top:809px;width:332px;height:300px;border:1px solid var(--line);background:#fff;text-align:center}
.sector-card h3{margin-top:136px;font:400 19px/1 "Open Sans",sans-serif;letter-spacing:.5px}
.sector-card .rule{width:42px;height:2px;background:var(--green);margin:13px auto 16px}
.sector-card p{font-size:13px;line-height:22px;color:var(--muted);padding:0 26px}
.diamond{position:absolute;width:141px;height:141px;transform:rotate(45deg);border:3px solid var(--green);box-shadow:4px 4px 0 #e6c200}

/* mission */
.mission{position:absolute;top:1149px;left:0;width:1200px;height:528px;background:linear-gradient(135deg,#2a6fbf 0%,#3a88d8 55%,#2978cc 100%);overflow:hidden}
.mission h2{position:absolute;top:82px;width:1200px;text-align:center;font:300 37px/1 "Roboto Slab",serif;color:#fff}
.mission h2 span{color:var(--yellow)}
.mission p{position:absolute;left:160px;width:880px;text-align:center;color:#fff;font-size:15px;line-height:27px}
.mission .btn{position:absolute;left:547px;top:333px}
.bulb{position:absolute;left:740px;top:330px;width:380px;height:198px;border-radius:50% 50% 40% 40%;background:radial-gradient(ellipse at 40% 40%,rgba(255,255,255,.85),rgba(200,230,190,.6) 45%,rgba(90,170,70,.45) 70%,rgba(255,255,255,0) 72%)}

/* services */
.services{position:absolute;top:1677px;left:0;width:1200px;height:755px;background:linear-gradient(180deg,#fff 0%,#f1f3f7 100%);overflow:hidden}
.collage{position:absolute;width:150px;height:150px;transform:rotate(45deg);border:4px solid #fff}
.service{position:absolute;left:638px;width:480px}
.service .icon{position:absolute;left:0;top:0}
.service h4{position:absolute;left:76px;top:0;font:400 17px/1 "Raleway",sans-serif;color:#2a6cb0;letter-spacing:.4px}
.service p{position:absolute;left:76px;top:32px;width:400px;font:400 12.5px/17px "Raleway",sans-serif;color:#777}
.skyline{position:absolute;left:0;top:536px;width:1200px;height:220px;background:linear-gradient(180deg,rgba(160,160,170,0) 0%,#b9bcc3 45%,#8b8f98 90%,#6d9a4c 100%)}

/* stats */
.stats{position:absolute;top:2432px;left:0;width:1200px;height:400px;background:var(--band);color:#fff}
.stat{position:absolute}
.stat b{display:block;font:400 40px/1 "Open Sans",sans-serif}
.stat small{display:block;margin-top:14px;font-size:13px}
.stats .divider-v{position:absolute;left:415px;top:58px;width:1px;height:260px;background:rgba(255,255,255,.25)}
.stats .divider-h{position:absolute;left:64px;top:194px;width:702px;height:1px;background:rgba(255,255,255,.25)}
.presence{position:absolute;left:811px;top:68px;width:340px}
.presence h3{font:400 18px/26px "Open Sans",sans-serif;letter-spacing:.5px}
.presence p{margin-top:30px;font-size:14px;line-height:22px}
.presence .btn{margin-top:24px}

/* footer */
.site-footer{position:absolute;top:2790px;left:0;width:1200px;height:393px}
.site-footer svg{position:absolute;top:0;left:0}
.foot-brand{position:absolute;left:82px;top:100px;font:700 38px/1 "Open Sans",sans-serif;color:var(--blue-light)}
.foot-about{position:absolute;left:82px;top:165px;width:380px;font-size:12px;line-height:22px;color:#aaa}
.foot-col h5{font:400 16px/1 "Open Sans",sans-serif;color:#fff;margin-bottom:22px}
.foot-col{position:absolute;color:#ddd;font-size:13px}
.contact-row{display:flex;margin-bottom:9px;line-height:18px}
.contact-row span:first-child{width:65px}
.newsletter-form{display:flex;margin-top:22px}
.newsletter-form .field{width:192px;height:36px;border:1px solid #666;background:#000;color:#777;font-size:11px;line-height:34px;padding-left:8px}
.newsletter-form .go{width:43px;height:36px;background:var(--blue-light);color:#fff;font-size:12px;font-weight:600;text-align:center;line-height:36px}
.foot-social{display:flex;gap:22px;margin-top:26px}
.foot-social span{width:13px;height:13px;border-radius:50%;background:#fff}
.foot-nav{position:absolute;top:285px;left:0;width:1200px;height:108px;background:var(--footer-deep);display:flex;justify-content:center;padding-top:30px;gap:38px}
.foot-nav a{color:#fff;font-size:12px;font-weight:600;text-decoration:none;height:16px}
.foot-nav a.active{color:var(--yellow)}
</style>
</head>
<body>

<section class="hero">
  <div class="hero-photo" role="img" aria-label="Solar panel field under a dramatic sunset sky"></div>
  <h1>All our energy is generated from renewable sources</h1>
  <p>Torvel-Solar: provides Solar Energy consulting services, Energy Efficiency Consulting services and Data Collection function. With services spanning the entire project lifecycle, Torvel scope goes beyond engineering, procurement and construction.</p>
  <a class="btn" href="#">KNOW MORE</a>
  <div class="dots"><span></span><span></span><span></span></div>
  <svg class="hero-wave" width="1200" height="70" viewBox="0 0 1200 70">
    <path d="M0 42 C300 8 700 10 1200 46 L1200 70 L0 70Z" fill="#fff"/>
    <path d="M0 40 C300 4 700 6 1200 42 L1200 50 C700 16 300 14 0 50Z" fill="var(--blue-dark)"/>
  </svg>
</section>

<header class="site-header">
  <svg width="1200" height="75" viewBox="0 0 1200 75">
    <defs><linearGradient id="navbar" x1="0" x2="1"><stop offset="0" stop-color="#2a6fb8"/><stop offset="1" stop-color="#3a82c6"/></linearGradient></defs>
    <rect width="1200" height="75" fill="url(#navbar)"/>
    <path d="M0 0 H350 L378 75 H0Z" fill="#fff"/>
  </svg>
  <div class="brand">TORVEL</div>
  <nav class="main-nav">
    <a class="active" href="#">HOME</a><a href="#">ABOUT</a><a href="#">CLIENTS</a><a href="#">PROJECTS</a><a href="#">TRAINING</a><a href="#">CARRER</a><a href="#">CONTACT</a>
  </nav>
  <div class="social" style="left:1000px;top:14px"><span></span><span></span><span></span><span></span></div>
</header>

<h2 class="section-title" style="top:627px">WE <em>ACTIVE</em> IN</h2>

<article class="sector-card" style="left:81px">
  <h3>RENEWABLE ENERGY</h3><div class="rule"></div>
  <p>The KSA (Saudi Arabia) solar market is a promising market with huge potential. The plan is to build 41,000 MW of solar in the coming 20 years</p>
</article>
<article class="sector-card" style="left:434px">
  <h3>PROCESS AUTOMATION</h3><div class="rule"></div>
  <p>We provide complete turnkey solutions for concept to commissioning of small solar PV power plant for any capacity for export to grid and off-grid sites, also for roof top installations.</p>
</article>
<article class="sector-card" style="left:785px">
  <h3>GENERAL ENGINEERING</h3><div class="rule"></div>
  <p>Provide Solar Energy consulting services, Energy Efficiency Consulting services and Data Collection function. With services spanning the entire project lifecycle, we scope goes beyond engineering.</p>
</article>
<div class="diamond" style="left:177px;top:735px;background:linear-gradient(160deg,#7fc4ee,#2a7cc2)" role="img" aria-label="Wind turbines against a blue sky"></div>
<div class="diamond" style="left:530px;top:735px;background:linear-gradient(160deg,#6aa6dc,#c4522e 70%)" role="img" aria-label="Solar panels on a tiled roof"></div>
<div class="diamond" style="left:881px;top:735px;background:linear-gradient(160deg,#1d5fb5,#7cc0f0)" role="img" aria-label="Close view of a solar cell grid"></div>

<section class="mission">
  <h2><span>TORVEL</span> MISSION &amp; VISION</h2>
  <p style="top:168px">To contribute to the GCC transformative change to the solar industry with focus on the connection between people, place, and technology.</p>
  <p style="top:245px">To become the GCC hub for solar knowledge and business creation (including photovoltaics (PV), CPV, concentrating solar power CSP and solar thermal technologies).</p>
  <a class="btn" href="#">KNOW MORE</a>
  <div class="bulb" role="img" aria-label="Light bulb with green grass growing inside"></div>
</section>

<section class="services">
  <div class="collage" style="left:259px;top:148px;background:linear-gradient(150deg,#6a9fd6,#27456e)" role="img" aria-label="Technician installing solar panels"></div>
  <div class="collage" style="left:117px;top:280px;background:linear-gradient(150deg,#d7e2c0,#8ba4b4)" role="img" aria-label="Engineers in hard hats reviewing plans"></div>
  <div class="collage" style="left:383px;top:280px;background:linear-gradient(150deg,#9bc8ef,#9c3c2a)" role="img" aria-label="Solar water heaters on a rooftop"></div>
  <div class="collage" style="left:255px;top:397px;background:linear-gradient(150deg,#8eb9e4,#e9e4dc)" role="img" aria-label="Hand dropping a coin into a piggy bank"></div>

  <div class="service" style="top:118px">
    <svg class="icon" width="54" height="54" viewBox="0 0 54 54"><circle cx="27" cy="27" r="10" fill="#5fb83a"/><g stroke="#2a8fd0" stroke-width="3" stroke-linecap="round"><path d="M27 4v8M27 42v8M4 27h8M42 27h8M11 11l6 6M37 37l6 6M43 11l-6 6M17 37l-6 6"/></g></svg>
    <h4>SOLAR ZONE INSTALLATION</h4>
    <p>We also provide complete turnkey solutions for concept to commissioning of small solar PV power plant for any capacity for export to grid and off-grid sites, also for roof top installations.</p>
  </div>
  <div class="service" style="top:276px">
    <svg class="icon" width="54" height="54" viewBox="0 0 54 54"><path d="M10 30a17 17 0 0 1 28-13" fill="none" stroke="#2a8fd0" stroke-width="4"/><rect x="28" y="24" width="16" height="20" rx="3" fill="#5fb83a"/><path d="M32 16v8M40 16v8M36 44v8" stroke="#5fb83a" stroke-width="3"/></svg>
    <h4>MAINTENANCE &amp; TRAINING</h4>
    <p>Through our internal workforce and partners, we include Design Engineering, Procurement, Construction, Commissioning, Operation, Maintenance and Training.</p>
  </div>
  <div class="service" style="top:435px">
    <svg class="icon" width="54" height="54" viewBox="0 0 54 54"><rect x="14" y="10" width="24" height="38" rx="3" fill="#2a8fd0"/><rect x="21" y="5" width="10" height="6" fill="#2a8fd0"/><rect x="18" y="24" width="16" height="20" fill="#5fb83a"/><path d="M27 27l-4 8h6l-4 7" stroke="#fff" stroke-width="2" fill="none"/></svg>
    <h4>ALTERNATIVE ENERGY SOURCES</h4>
    <p>Conduct pre-feasibility studies for solar project developers, studies cover technology selection, site assessments, transmission interconnection studies.</p>
  </div>
  <div class="skyline" role="img" aria-label="Row of solar panels in front of a city skyline and transmission tower"></div>
</section>

<section class="stats">
  <div class="stat" style="left:68px;top:95px"><b>4</b><small>Consecutive Awards for 2 years in a row</small></div>
  <div class="stat" style="left:443px;top:95px"><b>4</b><small>Innovation in Conservation of Energy</small></div>
  <div class="stat" style="left:68px;top:214px"><b>5000</b><small>Residential Installations</small></div>
  <div class="stat" style="left:443px;top:214px"><b>28</b><small>Corporate Groups</small></div>
  <div class="divider-v"></div>
  <div class="divider-h"></div>
  <div class="presence">
    <h3>OUR PRESENCE PROVES A POINT...</h3>
    <p>Our network of government officials, real estate experts, market analyst, and industry professionals track the market in real time, and turn knowledge to experience and value to our clients.</p>
    <a class="btn" href="#">KNOW MORE</a>
  </div>
</section>

<footer class="site-footer">
  <svg width="1200" height="393" viewBox="0 0 1200 393">
    <path d="M0 40 C400 -8 800 -8 1200 40 L1200 393 L0 393Z" fill="var(--footer)"/>
  </svg>
  <div class="foot-brand">TORVEL</div>
  <p class="foot-about">We are the solar experts in the solar kingdom. The KSA (Saudi Arabia) solar market is a promising market with huge potential. The plan is to build 41,000 MW of solar in the coming 20 years, as announced by N.R.E.A. (National Renewable Energy Authority). We provide our services.</p>
  <div class="foot-col" style="left:555px;top:85px">
    <h5>GET IN TOUCH</h5>
    <div class="contact-row"><span>PHONE:</span><span>+96 6130 555 014</span></div>
    <div class="contact-row"><span>EMAIL:</span><span>info@torvelpower.com</span></div>
    <div class="contact-row"><span>ADDRESS:</span><span>Harbor Road District 40210<br>Kingdom of Saudi Arabia</span></div>
  </div>
  <div class="foot-col" style="left:913px;top:85px">
    <h5>NEWSLETTER</h5>
    <div style="margin-top:-6px">Sign up your newsletter</div>
    <div class="newsletter-form"><div class="field">EMAIL ADRESS</div><div class="go">GO</div></div>
    <div class="foot-social"><span></span><span></span><span></span><span></span></div>
  </div>
  <nav class="foot-nav">
    <a class="active" href="#">HOME</a><a href="#">ABOUT</a><a href="#">CLIENTS</a><a href="#">PROJECTS</a><a href="#">TRAINING</a><a href="#">CAREER</a><a href="#">CONTACT</a>
  </nav>
</footer>

</body>
</html>
```